Is your Will up to date?

We need a flyer that invites people to ask themselves if their Will is up to date.
In addition it is a known fact that people do not adjust their Will as often as they should to reflect their current wishes and circumstances.
Also, a large number of people end up having their estate pay taxes
that could be avoided if correct planning is in place.
We are offering a free of charge service the carry out a check to make sure families have in place a Will that suits their needs and circumstances and that has taken into account the tax positions and impact fully with a view to having the estate as tax efficient as possible.
A Will service is also part of the family check up.

Below is the suggested text for the flyer

A Will is one of the most important documents that we should all have. Many people are aware that if they die without having made a Will, then intestate rules apply which means in simple terms, that family assets and cash could end up in the hands of the Treasury.

While many people have looked at and acted upon creating a Will, it is fair to say that for many, the terms and wishes of the Will are often outdated. It is easy to assume that amending a Will frequently is a complicated process which it need not be.

An individual or a family Will is most important in order to ensure that upon death, your estate is dealt with and distributed in accordance with your wishes. This is also to ensure that any family are looked after by those provisions. Not only may family changes and additions affect a family Will, but there are also life changing situations that can have an effect.

Additionally, consideration needs to be given regularly to the current tax position, with specific regard to Inheritance Tax and how estate values can be legitimately reduced resulting in less tax to pay.

At Hartwell & Company we have the advantage of our Chartered Accountancy practice background, as well as also being Independent Financial Advisers. We are therefore well placed to advise families on the creation or updating of their Will, and to give advice on how to minimise tax payments.

Even for individuals and families that have had no significant changes in circumstances for many years, very often the beneficiaries may need to be updated, and even the appointment of Executors and Trustees needs to be addressed because very often, these instructions are considerably out of date.

A Will and all of its complex implications should be reviewed every one or two years and it is an extremely simple process to do this with our assistance.

So far as minimising payments for tax there are a wide range of effective methods that help do this. As general examples, there can be gifts made to family or a partner, gifts to friends, charitable donations, the use of insurance products to help settle tax liability as well as looking at placing assets into Trust. We have a wealth of experience in setting up the different types of Trust that exist and can help you easily understand how they would work for you.

When looking at the preparation of a Will, there are hundreds of questions that could be considered appropriate. However, with our experience and knowledge, and bespoke software this process can be covered within an initial meeting of less than one hour. You will have the re-assurance of knowing that every aspect has been carefully considered in preparing a Will to your circumstances and wishes.

The initial meeting and any follow up meetings are completely free of all cost and charges, and can be held at either our offices, or at your home if preferred.

We can just as easily deal with the process over the telephone if more convenient. Thereafter, we will prepare a draft Will for you, and give you confirmation as to the charges. In most cases, an individual or family Will would not normally involve charges in excess of £100.

So far as mitigating possible Inheritance Tax liabilities on the estate, we also offer the benefit of an asset and investment review at no cost. The individual or family assets are carefully considered, along with your requirements of income and growth and any specific requests or wishes that you wish to build into any trust or other methods of your choosing.

At the initial meeting or conference call we discuss all of these implications and will prepare a report and recommendations for your consideration, again free of charge. If you decide to act upon any of the recommendations, then any fees can be discussed and agreed at that stage.

All in all, whether you require assistance in preparing or updating a Will, or receiving independent advice regarding your estate assets or investments, these functions are carried out by us at no initial costs or charges.

At every step of the way there are never hidden charges or fees that you will be asked to be paid. We have over 30 years of experience in these market places, and value the service we give our clients and the reputation we gain from it.

We consider the review of a Will should be carried out at a minimum of every two years and it is a very small financial budget to allow for, against having the satisfaction of knowing these important matters are reflecting your current views, circumstances and wishes.

The same can be said for any trust and investment matters and any estate advice given. We are extremely proud and confident of the service we provide, and if any of our clients decide they do not wish to act upon the advice given, then they at least have had the benefit of a thorough review together with a recommendation without obligations of any sort.

To discuss these matters further or to make arrangements for a meeting please call our offices or email to derek@hartwellco-mail.co.uk

Content will be uploaded with next 24 hours

I am updating the brief with the wording.
It needs to be spread over the front and back of the flyer in an easy to read non boring design

Our firm logo will be updated shorty plus our Institute logo
Please make the flyer as catchy and interesting as possible.
Its a relatively boring topic for most people so it has to be eye catching rather than reading a page in a book

We will increase the budget if we are presented with a design we really like

Please note slightly amended text uploaded today

Target Market(s)

middle to upper class residents

Industry/Entity Type

Investment

Requirements
Must have
• Web address
Easy to read and understand
To look and feel catchy and not like reading a book
Some catchy graphics about tax, money, families etc

Fields where I can easily insert text and other details

```html
<!DOCTYPE html>
<html lang="en">
<head>
<meta charset="utf-8">
<title>Is your Will up to date? – Hartwell &amp; Company</title>
<link rel="stylesheet" href="https://fonts.googleapis.com/css2?family=Cinzel:wght@400;600&family=Crimson+Text:wght@400;600&display=swap">
<style>
  :root{
    --red:#d7141e;
    --ink:#2b2b2b;
    --paper:#ffffff;
    --stage:#e6e6e6;
    --leaf:#8a9a4e;
  }
  *{box-sizing:border-box;margin:0;padding:0}
  html,body{width:1200px;height:847px;overflow:hidden;background:var(--stage)}
  .spread{position:relative;width:1200px;height:847px;display:flex}
  .page{position:relative;width:600px;height:847px;background:var(--paper);overflow:hidden;
    font-family:"Crimson Text",Georgia,serif;color:var(--ink);font-size:11.2px;line-height:1.32}
  .page--left{border-right:1px solid #ddd}
  .body-text p{margin-bottom:8px;text-align:justify}
  .caps{font-family:"Cinzel",Georgia,serif;font-weight:400;letter-spacing:.04em}

  /* left page */
  .left-copy{position:absolute;left:30px;top:46px;width:390px}
  .section-head{text-align:center;font-size:13px;line-height:1.35;margin:12px 0 14px}
  .left-band{position:absolute;left:0;bottom:0;width:430px;height:205px;background:var(--red)}
  .family-photo{position:absolute;left:30px;top:596px;width:390px;height:190px;
    background:linear-gradient(180deg,#b7c07a 0%,var(--leaf) 45%,#6f7b45 100%)}
  .call-line{position:absolute;left:30px;bottom:20px;color:#fff;font-size:15px;display:flex;align-items:center;gap:10px}
  .call-line svg{width:16px;height:16px}

  .title{position:absolute;left:440px;top:40px;width:150px;font-size:28px;line-height:1.22;color:#222}
  .title span{display:block}
  .title .l2{padding-left:4px}.title .l3{padding-left:6px}
  .title .l4{padding-left:10px}.title .l5{padding-left:12px}.title .l6{padding-left:14px}
  .title .hl{background:var(--red);color:#fff;padding:0 6px;display:inline-block}

  .pen-photo{position:absolute;background:
    radial-gradient(ellipse at 60% 40%,#8f8f8f 0%,#4a4a4a 55%,#262626 100%)}
  .pen-photo--left{left:430px;top:300px;width:170px;height:547px}
  .pen-photo--right{left:0;top:345px;width:178px;height:467px}

  /* right page */
  .right-head{position:absolute;left:20px;top:40px;width:320px;text-align:center;font-size:12.5px;line-height:1.35}
  .right-copy{position:absolute;left:20px;top:92px;width:320px}
  .right-copy-lower{position:absolute;left:192px;top:352px;width:240px}
  .pull-quote{position:absolute;left:358px;top:40px;width:220px;font-size:20px;line-height:1.3;color:#222}
  .right-band{position:absolute;left:0;bottom:0;width:600px;height:330px}
  .brand{position:absolute;right:28px;top:640px;background:#fff;padding:8px 14px;display:flex;align-items:center;gap:10px}
  .brand .mark{width:18px;height:18px;background:var(--red)}
  .brand .name{font-family:"Crimson Text",Georgia,serif;font-weight:600;font-size:17px;color:var(--ink);line-height:1}
  .brand .sub{font-size:9.5px;color:var(--ink);line-height:1.2}
  .web{position:absolute;right:28px;top:710px;color:#fff;font-size:13px;letter-spacing:.06em}
</style>
</head>
<body>
<main class="spread">
  <section class="page page--left">
    <div class="left-copy body-text">
      <p>A Will is one of the most important documents that we should all have. Many people are aware that if they die without a Will being in existence, then intestate rules apply which means in simple terms, that family assets and cash could end up in the hands of the Treasury.</p>
      <p>While many people have looked and acted upon creating a Will, it is fair to say that for the majority, the terms and wishes of the Will are often outdated. It is easy to assume that amending a Will frequently is a complicated process which it need not be.</p>
      <p>An individual or a family Will is most important in order to ensure that your estate is dealt with and distributed in accordance with your wishes upon death. This is also to ensure that any family are looked after by those provisions. Not only may family changes and additions affect a family Will, but there are also life changing situations that can have an affect.</p>
      <p>Additionally, consideration needs to be given on a regular basis to the current tax position, with specific regards to Inheritance Tax and how estate values can be legitimately reduced resulting in less tax to pay.</p>
      <h2 class="section-head caps">At Hartwell &amp; Company we have the advantage of our Chartered Accountancy practice background</h2>
      <p>At Hartwell &amp; Company we have the advantage of our Chartered Accountancy practice background, as well as also being Independent Financial Advisers. We are therefore well placed to advise families on the creation or updating of their Will, and to give advice on how to minimise tax payments.</p>
      <p>Even for individuals and families that have had no significant changes in circumstances for many years, very often the beneficiaries may need to be updated, some may need to be added, and even the appointment of Executors and Trustees need to be addressed because very often, these instructions are considerably out of date.</p>
    </div>
    <div class="left-band"></div>
    <div class="family-photo" role="img" aria-label="Photo of a smiling three-generation family sitting together outdoors in a park"></div>
    <p class="call-line caps">
      <svg viewBox="0 0 24 24" aria-hidden="true"><path fill="#fff" d="M6.6 10.8a15 15 0 0 0 6.6 6.6l2.2-2.2c.3-.3.7-.4 1-.2 1.1.4 2.3.6 3.6.6.6 0 1 .4 1 1V20c0 .6-.4 1-1 1A17 17 0 0 1 3 4c0-.6.4-1 1-1h3.5c.6 0 1 .4 1 1 0 1.3.2 2.5.6 3.6.1.3 0 .7-.2 1z"/></svg>
      Call us on 01632 960418
    </p>
    <h1 class="title caps">
      <span class="l1">Is</span>
      <span class="l2">your</span>
      <span class="l3"><span class="hl">Will</span></span>
      <span class="l4">up</span>
      <span class="l5">to</span>
      <span class="l6">date?</span>
    </h1>
    <div class="pen-photo pen-photo--left" role="img" aria-label="Close-up photo of a fountain pen nib on dark textured paper"></div>
  </section>

  <section class="page page--right">
    <h2 class="right-head caps">A Will and all of its complex implications should be reviewed every one or two years and it is an extremely</h2>
    <div class="right-copy body-text">
      <p>A Will is one of the most important documents that we should all have. Many people are aware that if they die without a Will being in existence, then intestate rules apply which means in simple terms, that family assets and cash could end up in the hands of the Treasury.</p>
      <p>While many people have looked and acted upon creating a Will, it is fair to say that for the majority, the terms and wishes of the Will are often outdated. It is easy to assume that amending a Will frequently is a complicated process which it need not be.</p>
      <p>An individual or a family Will is most important in order to ensure that your estate is dealt with and distributed in accordance with your wishes upon death. Not only may family changes and additions affect a family Will, but there are also life changing situations that can have an affect.</p>
      <p>Additionally, consideration needs to be given on a regular basis to the current tax position, with specific regards to Inheritance Tax and how estate values can be legitimately reduced resulting in less tax to pay.</p>
    </div>
    <p class="pull-quote caps">In most cases, an individual or family Will would typically not involve charges in excess of £100.</p>
    <div class="pen-photo pen-photo--right" role="img" aria-label="Continuation of the fountain pen nib photo"></div>
    <div class="right-copy-lower body-text">
      <p>At Hartwell &amp; Company we have the advantage of our Chartered Accountancy practice background, as well as also being Independent Financial Advisers. We are therefore well placed to advise families on the creation or updating of their Will, and to give advice on how to minimise tax payments.</p>
      <p>Even for individuals and families that have had no significant changes in circumstances for many years, very often the beneficiaries may need to be updated, some may need to be added, and even the appointment of Executors and Trustees need to be addressed because very often, these instructions are considerably out of date.</p>
      <p>A Will and all of its complex implications should be reviewed every one or two years and it is an extremely simple process to do this with our assistance.</p>
    </div>
    <svg class="right-band" viewBox="0 0 600 330" preserveAspectRatio="none" aria-hidden="true">
      <path fill="var(--red)" d="M178 175 C300 160 450 125 600 95 L600 330 L178 330 Z"/>
    </svg>
    <div class="brand">
      <span class="mark"></span>
      <div>
        <div class="name">Hartwell &amp; Co.</div>
        <div class="sub">Chartered Accountants &amp; Independent Financial Advisers</div>
      </div>
    </div>
    <p class="web caps">www.hartwellandco-advisers.co.uk</p>
  </section>
</main>
</body>
</html>
```